Flyer Design Project for The Verdance Studio

I'm a Naturopathic Herbalist who wishes to expand my business from x1 a week to x5 days a week and so need to produce a flyer to let people know what I do and to guide them to my website at theverdancestudio.com.au.
One-sided or double-sided A5 flyer on good quality paper for distribution by my referral network.  If all the info can fit on one side that would be great.
It would be great if the design could link up with my website i.e. the sun, mountains etc in the background but don't worry if not possible so then as an alternative I'd like to see something modern, fresh.
Otherwise it's to be simple, clean, easy to read, with a couple of relevant pictures if you want.

Target Market(s)
Predominantly females, from teens "clear skin tonics" to overloaded twenty-somethings, to pre-baby fertility programmes, healthy pregnancy etc
Industry/Entity Type
Business
Look and feel

```html
<!DOCTYPE html>
<html lang="en">
<head>
<meta charset="utf-8">
<title>Maren Holt DHM – Flyer</title>
<link rel="stylesheet" href="https://fonts.googleapis.com/css2?family=Arimo:wght@400;700&family=EB+Garamond:wght@400;600;700&display=swap">
<style>
  :root {
    --crimson: #a51d2d;
    --crimson-deep: #8f1624;
    --cream: #f1ebbf;
    --cream-pattern: #e4d9a8;
    --leaf-tan: #c4b287;
    --ink: #3b3225;
    --slate: #58595b;
    --white: #ffffff;
    --canvas: #ffffff;
  }
  * { box-sizing: border-box; margin: 0; padding: 0; }
  html, body { width: 1200px; height: 766px; overflow: hidden; background: var(--canvas); }
  .canvas { position: relative; width: 1200px; height: 766px; }

  .page { position: absolute; top: 0; height: 766px; overflow: hidden; }
  .page-front { left: 53px; width: 493px; background: var(--cream); border: 1px solid #222; border-top: 0; }
  .page-back { left: 652px; width: 548px; background: var(--cream); border-left: 1px solid #222; }

  /* front page */
  .edge-pattern { position: absolute; left: 0; top: 0; width: 28px; height: 382px;
    background: linear-gradient(180deg, var(--crimson-deep), var(--crimson)); }
  .hero-photo { position: absolute; left: 28px; top: 0; width: 465px; height: 330px;
    background: radial-gradient(ellipse at 45% 40%, #fffbe6 0%, #f4f1c9 35%, #c9dd8a 70%, #8fb84a 100%); }
  .practitioner-name { position: absolute; right: 60px; top: 266px; font-family: "Arimo", Arial, sans-serif;
    font-weight: 700; font-size: 31px; color: var(--slate); letter-spacing: -0.3px; }
  .practitioner-role { position: absolute; right: 60px; top: 304px; font-family: "Arimo", Arial, sans-serif;
    font-weight: 700; font-size: 14px; color: var(--slate); }
  .clinic-band { position: absolute; left: 0; top: 330px; width: 493px; height: 52px; background: var(--crimson);
    color: var(--white); font-family: "Arimo", Arial, sans-serif; font-size: 11.5px; text-align: center;
    line-height: 14.5px; padding: 5px 0 0 60px; }
  .side-pattern { position: absolute; left: 0; top: 382px; width: 84px; height: 343px; background: var(--cream-pattern); }
  .intro { position: absolute; left: 93px; top: 390px; width: 380px; font-family: "EB Garamond", Garamond, serif;
    color: var(--ink); font-size: 9.3px; line-height: 11.4px; }
  .intro .lead { text-align: center; margin-bottom: 3px; }
  .intro h2 { text-align: center; font-size: 15.5px; font-weight: 700; margin-bottom: 5px; }
  .intro p { margin-bottom: 4.5px; }
  .web-band { position: absolute; left: 0; top: 725px; width: 493px; height: 16px; background: var(--crimson);
    color: var(--white); font-family: "Arimo", Arial, sans-serif; font-size: 10.5px; line-height: 16px;
    text-align: center; padding-left: 60px; }

  /* back page */
  .back-pattern { position: absolute; inset: 0; background: var(--cream-pattern); }
  .tonic-panel { position: absolute; left: 87px; top: 0; width: 374px; height: 594px; background: var(--crimson);
    padding: 51px 30px 0 37px; color: var(--white); font-family: "EB Garamond", Garamond, serif; }
  .tonic { margin-bottom: 17px; }
  .tonic h3 { position: relative; font-size: 13px; font-weight: 700; margin-bottom: 6px; }
  .tonic h3::before { content: ""; position: absolute; left: -27px; top: 5px; width: 13px; height: 7px; background: var(--white); }
  .tonic p { font-size: 10.3px; line-height: 15px; }
  .express-box { position: absolute; left: 87px; top: 594px; width: 374px; height: 140px; background: var(--cream);
    font-family: "EB Garamond", Garamond, serif; color: var(--ink); text-align: center; padding: 10px 18px 0; font-size: 9.5px; line-height: 13.5px; }
  .express-box h4 { font-size: 11.5px; font-weight: 600; letter-spacing: 0.3px; margin-bottom: 4px; }
  .express-box p { margin-bottom: 7px; }
  .back-band { position: absolute; left: 87px; top: 734px; width: 374px; height: 32px; background: var(--crimson); }
</style>
</head>
<body>
<div class="canvas">

  <section class="page page-front">
    <div class="edge-pattern" role="img" aria-label="Crimson band with a faint leaf pattern"></div>
    <div class="hero-photo" role="img" aria-label="Photo of a serene woman with closed eyes beside fresh green bamboo leaves"></div>
    <h1 class="practitioner-name">Maren Holt DHM</h1>
    <p class="practitioner-role">Local Naturopathic Herbalist</p>
    <div class="clinic-band">
      joins the professional team at Willow Grove Clinic<br>
      48 Fernleigh Road, Bramblewood, NSW, 2099<br>
      0400 123 456
    </div>
    <div class="side-pattern" role="img" aria-label="Tan leaf and flower pattern on cream"></div>
    <div class="intro">
      <p class="lead">Are you feeling tired, run down, under the weather or simply just feeling out of balance?</p>
      <h2>Herbal Medicine could be the answer for you.</h2>
      <p>Maren has a wealth of experience with over 14 years in clinical practice which, coupled with a great deal of “life experience” as the mother of three children, helps to make your consultation professional, caring and healing.</p>
      <p>Passionate about helping you reach your highest potential health-wise, Maren will make you a “Daily Wellness Tonic” which is like the best multi-vitamin you could have as it’s tailor-made especially for you. The “Daily Wellness Tonic” can help strengthen, nourish, heal and rebalance your whole body.</p>
      <p>“Daily Wellness Tonics” can be made to assist you keeping yourself well, for nurturing yourself (so in turn you can nurture others), for re-energising you, for aging gracefully, to assist you feeling back on top of life and to help you face challenges more easily.</p>
      <p>Herbal medicine can help with Sleep Disorders, Weak Immune Systems, Anxiety, Depression, Fertility issues, Childhood Diseases, Skin Problems, Gastro-Intestinal Disorders and Women’s Health.</p>
      <p>Maren also specialises in “Super Immune Boost Tonics” assisting with acute conditions such as coughs, colds, sore throats and offers 20-30 minute “Express Appointments”. Useful as a preventative measure or as a way of healing these conditions more quickly.</p>
      <p>“Clear Skin Wellness Tonics” are popular with teens and a special teen package is also offered as an “Express Appointment” with a bottle of tonic.</p>
      <p>For more information, check out The Verdance Studio</p>
    </div>
    <div class="web-band">website at www.theverdancestudio.com.au</div>
  </section>

  <section class="page page-back">
    <div class="back-pattern" role="img" aria-label="Tan leaf and flower pattern on cream"></div>
    <div class="tonic-panel">
      <article class="tonic">
        <h3>Clear Skin Wellness Tonic</h3>
        <p>Clear skin begins with a healthy liver. The Clear Skin Wellness Tonic treats the liver, stimulates the lymphatic system, the circulation and the skin. Useful when hormones are disordered especially for teenagers and at times of hormonal loading.</p>
      </article>
      <article class="tonic">
        <h3>Super Immune Boosting Wellness Tonic</h3>
        <p>An immune system tonic to strengthen and enable your body to fight off infection from colds, flu, sore throats, chest infections and sinus problems. The tonic is made specifically for you and your constitution.</p>
      </article>
      <article class="tonic">
        <h3>Peaceful Sleep Wellness Tonic</h3>
        <p>For peaceful, rejuvenative sleep. Helps relieve insomnia. The tonic is made for your specific condition and heals the root cause of why you’re not sleeping well. Can be used in conjunction with “Knock Out Sleep Tonic” to help ease you into time zones more quickly when travelling.</p>
      </article>
      <article class="tonic">
        <h3>Energy &amp; Vitality Wellness Tonic</h3>
        <p>The Energy &amp; Vitality Wellness Tonic is popular with anyone doing any kind of sport or physical training. It helps you to recover more quickly after a workout. It can also help strengthen muscles and ligaments. A great way to achieve safe, fast, natural energy and vitality.</p>
      </article>
      <article class="tonic">
        <h3>Liver Wellness Tonic</h3>
        <p>Useful for any kind of liver damage from alcohol, drugs, infection, bad diet or emotional trauma. Can help to detoxify your liver, improve liver (and gall bladder) function, improve emotional handling, allergies and balance menstrual cycles.</p>
      </article>
    </div>
    <div class="express-box">
      <h4>EXPRESS CONSULTATIONS</h4>
      <p>Available for acute conditions such as colds, flu, sore throats, chest infections and generally feeling “unwell”.</p>
      <p>Contact Maren Holt on 0400 123 456 for a consultation at The Verdance Studio, c/- Willow Grove Clinic, 48 Fernleigh Road, Bramblewood, NSW 2099.</p>
      <p>For more information check out the website at<br>theverdancestudio.com.au.</p>
    </div>
    <div class="back-band"></div>
  </section>

</div>
</body>
</html>
```